Electrician Flyer

Hi, I will provide all information needed for the flyer, just needing a cool design for a double sided flyer. Happy for a designer to play around with pictures, text, headings, boarders. The flyer will be standard size (A5). I have also uploaded a example flyer which I quite liked as a rough guide. Thanks

Target Market(s)

Adults

Industry/Entity Type

Electrician

Requirements
Must have
• Hi, I have uploaded some documents showing information needed on each side of the flyer (1st side of flyer, 2nd side of flyer). i am wanting the flyer to stand out and look professional. please add some images and possible stick to the color schemes of my logo,
Nice to have
• I have a plug type image on my Van, I was hoping to include this somewhere on the flyer. I have attached an image of the van for reference. Maybe image of a light bulb or something to make it less text heavy.

```html
<!DOCTYPE html>
<html lang="en">
<head>
<meta charset="utf-8">
<title>Voltcrest Electrical &amp; Communications Flyer</title>
<link href="https://fonts.googleapis.com/css2?family=Open+Sans:wght@400;600;700;800&display=swap" rel="stylesheet">
<style>
  :root {
    --brand-blue: #0a55a8;
    --brand-blue-deep: #064a97;
    --brand-green: #9bc31c;
    --night-top: #1d2b3c;
    --night-mid: #15120f;
    --deck-warm: #3a2a1e;
    --silver-light: #f4f4f4;
    --silver-dark: #a9a9a9;
    --tagline-grey: #c9ccd0;
    --white: #ffffff;
  }
  * { margin: 0; padding: 0; box-sizing: border-box; }
  html, body { width: 846px; height: 1200px; overflow: hidden; background: #ffffff; }
  .flyer {
    position: relative;
    width: 846px;
    height: 1200px;
    overflow: hidden;
    font-family: "Open Sans", Arial, sans-serif;
    background: linear-gradient(180deg, var(--silver-light) 0%, #dcdcdc 55%, var(--silver-dark) 100%);
  }
  .hero-photo {
    position: absolute;
    left: 0; top: 0;
    width: 846px; height: 920px;
    background:
      radial-gradient(ellipse 160px 200px at 130px 190px, rgba(230,190,120,0.55), transparent 70%),
      radial-gradient(ellipse 300px 120px at 420px 420px, rgba(120,85,55,0.45), transparent 75%),
      radial-gradient(ellipse 80px 30px at 460px 355px, rgba(60,150,230,0.55), transparent 80%),
      linear-gradient(180deg, var(--night-top) 0%, #1a1f26 25%, var(--night-mid) 45%, var(--deck-warm) 60%, #1a1410 80%, #141414 100%);
  }
  .brand {
    position: absolute;
    right: 56px; top: 48px;
    text-align: right;
  }
  .brand-name {
    font-size: 92px;
    font-weight: 800;
    line-height: 1;
    letter-spacing: 2px;
    color: var(--brand-blue);
  }
  .brand-tagline {
    margin-top: 10px;
    font-size: 22px;
    font-weight: 400;
    letter-spacing: 6.2px;
    color: var(--tagline-grey);
  }
  .headline {
    position: absolute;
    right: 56px; top: 238px;
    text-align: right;
    color: var(--brand-green);
    font-weight: 700;
    text-shadow: 2px 2px 3px rgba(0,0,0,0.6);
  }
  .headline-main { font-size: 58px; line-height: 1.1; }
  .headline-sub { font-size: 37px; line-height: 1.1; }
  .swoosh {
    position: absolute;
    left: 0; top: 760px;
    width: 846px; height: 440px;
  }
  .services {
    position: absolute;
    left: 58px; top: 584px;
    width: 408px; height: 558px;
    background: var(--brand-blue);
    border-radius: 8px;
    overflow: hidden;
  }
  .services-title {
    height: 57px;
    background: var(--brand-green);
    color: var(--white);
    font-size: 27px;
    font-weight: 700;
    text-align: center;
    line-height: 57px;
  }
  .services-list {
    list-style: none;
    padding: 23px 0 0 24px;
  }
  .services-list li {
    color: var(--white);
    font-size: 23.5px;
    font-weight: 700;
    line-height: 28.3px;
    white-space: nowrap;
  }
  .services-list li::before {
    content: "\00B7";
    display: inline-block;
    width: 21px;
  }
  .contact {
    position: absolute;
    left: 530px; top: 942px;
    color: var(--brand-blue-deep);
    font-size: 21.5px;
    line-height: 28.3px;
  }
  .contact-phone {
    font-size: 29px;
    font-weight: 700;
    line-height: 40px;
  }
  .contact-licence { margin-top: 28px; }
</style>
</head>
<body>
<div class="flyer">
  <div class="hero-photo" role="img" aria-label="Night-time photo of a timber deck beside a house with glowing windows, lit by small deck lights and a blue-lit pool"></div>

  <div class="brand">
    <div class="brand-name">VOLTCREST</div>
    <div class="brand-tagline">ELECTRICAL &amp; COMMUNICATIONS</div>
  </div>

  <div class="headline">
    <div class="headline-main">Guaranteed</div>
    <div class="headline-sub">workmanship<br>you can rely on</div>
  </div>

  <svg class="swoosh" viewBox="0 0 846 440" preserveAspectRatio="none" aria-hidden="true">
    <defs>
      <linearGradient id="silver" x1="0" y1="0" x2="0" y2="1">
        <stop offset="0" stop-color="#f6f6f6"/>
        <stop offset="0.6" stop-color="#dedede"/>
        <stop offset="1" stop-color="#aaaaaa"/>
      </linearGradient>
    </defs>
    <path d="M0 22 C 150 90, 330 150, 520 148 C 640 146, 760 135, 846 122 L846 440 L0 440 Z" fill="#0a55a8"/>
    <path d="M0 52 C 150 115, 330 165, 520 162 C 640 160, 760 150, 846 140 L846 440 L0 440 Z" fill="url(#silver)"/>
    <path d="M466 146 C 600 146, 740 134, 846 116" fill="none" stroke="#9bc31c" stroke-width="6"/>
  </svg>

  <section class="services">
    <h2 class="services-title">OUR SERVICES</h2>
    <ul class="services-list">
      <li>Electrical Property Reports</li>
      <li>Bathroom Heat Lights</li>
      <li>Bore &amp; Pump Connections</li>
      <li>House Re-wires</li>
      <li>Oven/Stove Installations</li>
      <li>Renovations/Extensions</li>
      <li>Security Lights &amp; Systems</li>
      <li>Test &amp; Tagging</li>
      <li>Power Points</li>
      <li>LED &amp; Lighting</li>
      <li>Safety Switches</li>
      <li>Switchboard upgrades</li>
      <li>TV Points</li>
      <li>Phone &amp; Data Points</li>
      <li>Fans &amp; Ducting</li>
      <li>Maintenance &amp; Repair</li>
    </ul>
  </section>

  <address class="contact" style="font-style: normal;">
    <div class="contact-phone">0400 123 456</div>
    <div>www.voltcrest.com.au</div>
    <div>info@voltcrest.com.au</div>
    <div>PO BOX 512 ARDEN</div>
    <div class="contact-licence">EC 20485</div>
    <div>ACN: 12 345 678 901</div>
  </address>
</div>
</body>
</html>
```